Progressive business consultancy seeking "Accounting Industry Flyer"

We are looking for an industry flyer that we will use with potential clients/prospects that outlines our skills and experience in delivering change across the Accounting Services Industry. The flyer will be used to help potential clients understand the challenges and issues faced by the accounting industry and how our service offerings can help them solve their project challenges and problems.

About Us:
Based in Melbourne, Australia, Vendor-o is a management consulting organisation that partners with their clients to lead the execution of strategic process and system improvement initiatives.

Vendor-o offers business advisory services in Project Management, Business Process Management, Change Management, Business Analysis and Business Intelligence. Vendor-o combines hands on delivery with coaching in best practice methodologies and approaches to build our clients capabilities ensuring their ongoing success in project implementations.

Vendor-o has extensive experience across a wide range of industries. We specialise in assisting organisations across the accounting, legal, financial services and health sectors.

Our core purpose is to help businesses in the middle market navigate transformational change through clear and focused execution and enablement.

www.vendor-o.com.au
@vendor_o

What we're looking for:

A professional, corporate, industry flyer providing an overview of our capabilities and experience in the accounting industry. Focus is on the "e" in vendor-o. The look should be sharp and crisp, with a professional and corporate feel. The target for the flyer is Accountants and Mid-Tier Accounting Firms.

The Vendor-o colours are white and blue (RGB:0/86/162 and
CMYK 97/73/4/0)

A professional, corporate theme that is consistent across both sides of the flyer. The design should reflect our focus on the "e" in vendor-o, which is what we're really about - "e"xecution and "e"nablement of change.

I've attached a PNG file of our word template which shows the focus on the "e" as a watermark on the document as well as the font files if required.

Let me know if you need any further information or design specifics.

Thanks,

Felicity
(on behalf of Gregory)
Updates

Hi All, Thanks for your design submissions so far. We have discovered that our hero image has not been attached to the brief. Please find the jpeg attached now. It has been loaded as "Vendor-o Hero Image.jpg" Thanks Gregory @vendor_o

Reason: Hi Designers, Thanks to everyone who has taken the time to make a submission on our contest. We really appreciate it. We have decided to extend our deadline by 5 days so we can review the designs with other colleagues and provide feedback to everyone who has made a submission. Thanks for all your creative designs. Gregory @vendor_o

Reason: Hi designers, thanks to everyone for taking the time to submit their designs. We are going to have to extend our deadline again as we haven't had an opportunity to review all of the designs properly and provide feedback.

Target Market(s)

Accountants and Accounting Firms (mid tier firms)

Industry/Entity Type

Management Consulting

Font styles to use
Other font styles liked:
• Calibri & Attached font files.

Colors
0455a3
3277b5
ffffff

Requirements
Must have
• A Professional A4 double sided colour flyer consisting of:
• Front Page:
• - hero image (attached)
• - Draft content front (attached)
• - Vendor-o Logo (attached)
• Back Page
• - Draft content back (attached)

```html
<!DOCTYPE html>
<html lang="en">
<head>
<meta charset="utf-8">
<title>Vendor-o Accounting Industry Flyer</title>
<link rel="stylesheet" href="https://fonts.googleapis.com/css2?family=Carlito:wght@400;700&family=Arimo:wght@700&display=swap">
<style>
  :root {
    --brand-blue: #0455a3;
    --brand-blue-light: #3277b5;
    --white: #ffffff;
    --ink: #3a3a3a;
    --panel-grey: #e5e6e8;
    --rule-grey: #8a8d91;
    --hero-dark: #1c1e22;
  }
  * { margin: 0; padding: 0; box-sizing: border-box; }
  html, body { width: 848px; height: 1200px; overflow: hidden; background: var(--white); }
  body { font-family: "Carlito", "Calibri", sans-serif; color: var(--ink); }
  .flyer { position: relative; width: 848px; height: 1200px; overflow: hidden; background: var(--white); }

  /* Header */
  .brand-name {
    position: absolute; left: 64px; top: 28px;
    font-family: "Carlito", "Calibri", sans-serif; font-weight: 400;
    font-size: 78px; line-height: 1; color: var(--brand-blue); letter-spacing: 1px;
  }
  .company-details {
    position: absolute; left: 620px; top: 38px; height: 82px;
    border-left: 1px solid var(--rule-grey); padding-left: 18px;
    font-size: 14px; line-height: 19px; color: var(--ink);
  }
  .company-details .company-name { color: var(--brand-blue); font-size: 17px; margin-bottom: 2px; display: block; }

  /* Hero */
  .hero {
    position: absolute; left: 0; top: 138px; width: 848px; height: 333px;
    background: var(--hero-dark);
  }
  .hero-image {
    position: absolute; left: 0; top: 0; width: 560px; height: 333px;
    background: radial-gradient(ellipse at 55% 40%, #6a737c 0%, #3b4249 40%, #1c1e22 85%);
  }
  .hero-title {
    position: absolute; left: 551px; top: 132px; width: 290px;
    font-family: "Arimo", "Arial", sans-serif; font-weight: 700;
    font-size: 29.5px; line-height: 37px; color: var(--white);
  }

  /* Section headings */
  .section-heading {
    display: flex; align-items: flex-start; gap: 5px;
    font-weight: 700; font-size: 17.5px; line-height: 20px; color: var(--brand-blue);
  }
  .section-heading svg { flex: none; margin-top: 3px; }
  p { font-size: 11.4px; line-height: 14.2px; text-align: justify; }

  /* Left column */
  .main-column { position: absolute; left: 36px; top: 497px; width: 454px; }
  .main-column .section-heading { margin-bottom: 9px; }
  .main-column p + p { margin-top: 10px; }
  .main-column section + section { margin-top: 16px; }
  .challenges p + p { margin-top: 14px; }

  /* Right column panels */
  .side-panel {
    position: absolute; left: 515px; width: 298px;
    background: var(--panel-grey); border-radius: 14px; padding: 16px 16px 14px 16px;
  }
  .side-panel .section-heading { margin-bottom: 8px; }
  .panel-help { top: 490px; height: 421px; }
  .panel-case { top: 926px; height: 219px; }
  .panel-help .delivery { margin-top: 14px; }
  .delivery-list { list-style: none; margin-top: 12px; padding-left: 6px; }
  .delivery-list li {
    position: relative; padding-left: 18px; font-size: 11.6px; line-height: 14.4px; margin-bottom: 10px;
  }
  .delivery-list li::before {
    content: ""; position: absolute; left: 1px; top: 4px; width: 6px; height: 6px;
    border-radius: 50%; background: var(--brand-blue);
  }

  /* Footer */
  .footer {
    position: absolute; left: 0; top: 1160px; width: 848px; height: 40px;
    background: var(--brand-blue); color: var(--white);
    display: flex; align-items: center; padding-left: 36px;
    font-weight: 700; font-size: 13.5px;
  }
  .contact { display: flex; align-items: center; gap: 6px; margin-right: 20px; }
  .contact-badge {
    width: 16px; height: 16px; border-radius: 50%; background: var(--white);
    color: var(--brand-blue); font-size: 10px; font-weight: 700;
    display: flex; align-items: center; justify-content: center;
  }
  .website { position: absolute; right: 42px; font-size: 18px; }
</style>
</head>
<body>
<div class="flyer">

  <header>
    <div class="brand-name">Vendor-o</div>
    <address class="company-details" style="font-style: normal;">
      <span class="company-name">Vendor-o Pty Limited</span>
      Level 12, 48 Harbour Street<br>
      Melbourne 3000, Victoria
    </address>
  </header>

  <div class="hero">
    <div class="hero-image" role="img" aria-label="Businessman in a dark suit touching a glowing cloud icon linked to a network of technology icons"></div>
    <h1 class="hero-title">Helping your business navigate transformational change</h1>
  </div>

  <main class="main-column">
    <section>
      <h2 class="section-heading">
        <svg width="13" height="13" viewBox="0 0 13 13" aria-hidden="true"><circle cx="6.5" cy="6.5" r="5.6" fill="none" stroke="currentColor" stroke-width="1.3"/><path d="M5 3.8 L8.6 6.5 L5 9.2 Z" fill="currentColor"/></svg>
        Who are Vendor-o?
      </h2>
      <p>Based in Melbourne, Australia, Vendor-o is a management consulting organisation who partner with their clients to lead the execution of strategic process and system improvement initiatives. Our core purpose is to help your business navigate transformational change through clear and focused execution and enablement.</p>
      <p>Vendor-o has proven experience leading change and delivering improvements to organisations across a range of industries. However, we specialise in working with accounting firms in the middle market helping them to navigate the disruptive changes rapidly changing the face of their industry. Our expertise includes business process automation and the management of onshore and offshore teams across tax and audit compliance services.</p>
    </section>

    <section>
      <h2 class="section-heading">
        <svg width="13" height="13" viewBox="0 0 13 13" aria-hidden="true"><circle cx="6.5" cy="6.5" r="5.6" fill="none" stroke="currentColor" stroke-width="1.3"/><path d="M5 3.8 L8.6 6.5 L5 9.2 Z" fill="currentColor"/></svg>
        What are our capabilities?
      </h2>
      <p>We offer a range of project advisory services including project management, business process improvement, change management, business analysis and business intelligence. At Vendor-o we aim to build your organisation’s capabilities enabling you to manage and execute change initiatives. We do this by providing hands-on project delivery along with coaching in best practice project methodologies. We look to establish simple repeatable project and change management processes that can continue to be utilised by your organisation long into the future.</p>
    </section>

    <section class="challenges">
      <h2 class="section-heading">
        <svg width="13" height="13" viewBox="0 0 13 13" aria-hidden="true"><circle cx="6.5" cy="6.5" r="5.6" fill="none" stroke="currentColor" stroke-width="1.3"/><path d="M5 3.8 L8.6 6.5 L5 9.2 Z" fill="currentColor"/></svg>
        <span>What are the major challenges facing the<br>accounting industry?</span>
      </h2>
      <p>The three major disruptors facing accounting firms are the offshoring of compliance activities, rapid changes in technology and the internet. These industry wide disruptors are placing pressure on fee negotiations, revenue generation and are also providing a significant increase in competitive activity. As clients continue to push prices down, accounting firms have and/or are in the process of implementing systems and technologies to drive further efficiencies and reduce costs. In addition the outsourcing of accounting services for low end and non-confidential work to further lower client costs has been pervasive. This has now started to extend across end to end tax and audit compliance processes as firms start to recognise the qualified accounting capability they have available to them at a much lower cost.</p>
      <p>The need to win new business and increased competition has resulted in the entry of the Big 4 into the middle tier market and the emergence and expansion of non-traditional competitors with different business models. Cloud computing is enabling businesses to scale at a very rapid rate and maintain low cost operating models. As the industry becomes hyper-competitive it is crucial for accounting firms to deepen their understanding of clients and build their capability to offer value added advisory services.</p>
    </section>
  </main>

  <aside class="side-panel panel-help">
    <h2 class="section-heading">
      <svg width="13" height="13" viewBox="0 0 13 13" aria-hidden="true"><circle cx="6.5" cy="6.5" r="5.6" fill="none" stroke="currentColor" stroke-width="1.3"/><path d="M5 3.8 L8.6 6.5 L5 9.2 Z" fill="currentColor"/></svg>
      <span>How we can help<br>professional services firms in<br>the accounting industry</span>
    </h2>
    <p>Vendor-o have deep industry experience gained across the Big 4 and mid-tier accounting firms and a consistent track record for leading change and delivering improvements to business processes. Our people have extensive industry experience leading and managing teams at organisations such as Northgate Partners, Hollis Brandt, RQT Group, Calder Accountants, Meridian Advisers and Ashcombe Partners.</p>

    <h2 class="section-heading delivery">
      <svg width="13" height="13" viewBox="0 0 13 13" aria-hidden="true"><circle cx="6.5" cy="6.5" r="5.6" fill="none" stroke="currentColor" stroke-width="1.3"/><path d="M5 3.8 L8.6 6.5 L5 9.2 Z" fill="currentColor"/></svg>
      <span>Our delivery model involves us working directly alongside you helping you to:</span>
    </h2>
    <ul class="delivery-list">
      <li>Recognise the major disruptors for your business</li>
      <li>Ensure you have developed a clear strategy on how to respond</li>
      <li>Develop a plan and execute the changes required to ensure business growth is maintained and the quality of your client work is not compromised</li>
    </ul>
  </aside>

  <aside class="side-panel panel-case">
    <h2 class="section-heading">
      <svg width="13" height="13" viewBox="0 0 13 13" aria-hidden="true"><circle cx="6.5" cy="6.5" r="5.6" fill="none" stroke="currentColor" stroke-width="1.3"/><path d="M5 3.8 L8.6 6.5 L5 9.2 Z" fill="currentColor"/></svg>
      Case Study
    </h2>
    <p>A leading mid-tier accounting firm required support to implement large scale process and system improvements identified through a major organisational review. Through a structured program delivery approach we harnessed the required internal resources, engaged widely across the organisation and delivered major changes throughout the firm every 8 weeks with minimal disruption to normal business operations. The implementation of these improvements freed up over x hours per annum that could be redirected to value added advisory services.</p>
  </aside>

  <footer class="footer">
    <span class="contact"><span class="contact-badge">E</span>enquiries@vendor-o.com.au</span>
    <span class="contact"><span class="contact-badge">P</span>(+61) 3 9555 0142</span>
    <span class="contact"><span class="contact-badge">F</span>(+61) 3 9555 0187</span>
    <span class="website">www.vendor-o.com.au</span>
  </footer>

</div>
</body>
</html>
```